Women's Jewellery startup needs a captivating, beautifully designed and intuitive online store

[12/24 update]

Added 2 additional documents:

Feedback on designs received so far: designer feedback.docx
Product images from catalogue: products images.docx

Please read the feedback provided on designs provided so far to guide you further on your submission. The product images can be used to create promotional banners for the site.

@@@Added a document (VELISTO JEWELLERY_checklist.docx) which can be used by designers as a checklist when submitting their designs to ensure all aspects of the requirements have been covered @@@

+++IMPORTANT BUT NOT SPECIFIED IN THE REQUIREMENTS DOCUMENT - DESIGN SHOULD INCLUDE SUPPORT FOR MOBILE FRIENDLY SITE TOO+++

***Previous experience designing Jewellery online stores preferred (not essential)***

The name of the online Jewellery store is "Velisto Jewellery" and the business is based in Hong Kong. It will be run by 2 stay at home mothers. We need a Shopify themed store designed that will achieve the following objectives in order of priority:

• Conversion: The primary objective of the design/content is to prompt the customer to make a purchase. While this may sound obvious, it is mentioned so as not to distract the design process by focusing on other objectives (which are also important). The site also needs to be optimized so as to rank high in search engine searches for relevant keywords (SEO)
• Navigation: An intuitive interface which takes away a lot of the thinking from the customer by making it obvious what they need to do when they visit the store
• Engagement: Encourages the customer to spend time on the website and share content with their social network

Where applicable, the design of the store should reflect as closely as possible the mission statements and words outlined below:

• Jewellery you’ll fall in love with
• We want every client to leave the store with a smile
• We want to be able to provide the best service we can in every situation no matter what
• We aim to increase our business by word of mouth; therefore we tell people things about our store that makes it interesting for them to share
• We love every customer, no matter how difficult things get
• We, as a team, are so well informed about our products and brands that we always have the best information for our customers
• We celebrate women here!
• We celebrate life in here!
• We celebrate beauty here!
• We celebrate families here, as jewellery often stays within families.
• We will always try to make an extra step
• We will always try to exceed the expectation of our customers
• We will go as far as we possibly can to attract a customer back to our store and connect with us
• Every client that leaves our store knows more about jewellery because we passionately told him about it
• Romantic, classic, love, warm, cool, stylish

A draft functional specification is attached with this brief. We would like the design to reflect as closely as possible the functional requirements outlined in the document. Open to suggestions to improve upon the functional requirements.

Low design quality

Target Market(s)

Women aged 18-55

Industry/Entity Type

Jewelry Store

Coding

Coded - Design and coding required

Number of Pages Required

5+ page

Font styles to use
Other font styles liked:
• Myriad Pro as per Logo but open to any font that complements this one

Requirements
Must have
• 1. A look that encourages the user to make a purchase
• 2. An intuitive, easy to navigate and engaging interface
• 3. Primary colour scheme as defined in the functional specification attached
• 4. Simplistic look, not too cluttered
Nice to have
• 1. Closely matching the functional requirements of the site as outlined in the requirements specification but open to any better ideas

```html
<!DOCTYPE html>
<html lang="en">
<head>
<meta charset="utf-8">
<title>Velisto Jewellery</title>
<link href="https://fonts.googleapis.com/css2?family=Open+Sans:wght@400;600;700;800&display=swap" rel="stylesheet">
<style>
:root{
  --gold:#c59d5f;
  --gold-dark:#a97f3f;
  --gold-soft:#e3c98f;
  --silver:#c9ccd1;
  --ink:#1c1c1c;
  --text:#444;
  --muted:#777;
  --soft:#f1f1f1;
  --line:#e2e2e2;
  --footer:#1e1e1e;
  --white:#fff;
}
*{box-sizing:border-box;margin:0;padding:0}
html,body{width:1200px;height:2609px;overflow:hidden}
body{position:relative;background:var(--white);font-family:"Open Sans",Arial,sans-serif;color:var(--text)}
.abs{position:absolute}

/* header */
.site-header{left:0;top:0;width:1200px;height:122px;background:var(--white)}
.brand{left:249px;top:40px;display:flex;align-items:center;gap:10px;font-weight:700;font-size:22px;letter-spacing:4px;color:var(--gold)}
.brand-dot{width:14px;height:14px;border-radius:50%;background:var(--gold)}
.main-nav{left:483px;top:52px;font-size:13px;color:#555}
.main-nav a{color:inherit;text-decoration:none;position:absolute;white-space:nowrap}
.header-icons svg{position:absolute}

/* dropdown */
.account-menu{left:783px;top:122px;width:168px;height:254px;background:var(--white);box-shadow:0 3px 12px rgba(0,0,0,.18);z-index:5;padding:14px 20px;font-size:9px;color:#555}
.account-menu h4{font-size:9px;color:var(--gold);font-weight:700;margin-bottom:8px}
.account-menu ul{list-style:none;padding-left:14px;line-height:17.5px}
.account-menu hr{border:0;border-top:1px solid var(--line);margin:4px 0 0}
.account-menu .sec{margin-top:10px}

/* hero */
.hero{left:0;top:122px;width:1200px;height:508px;background:#000}
.hero-photo{left:496px;top:0;width:704px;height:508px;background:linear-gradient(90deg,#000 0%,#3a251b 30%,#7a5443 55%,#3a2419 80%,#120b08 100%)}
.hero-tag{left:249px;top:151px;width:160px;height:40px;background:var(--gold);color:var(--white);font-weight:800;font-size:24px;letter-spacing:1px;text-align:center;line-height:40px}
.hero-title{left:249px;top:196px;color:var(--white);font-weight:800;font-size:52px;line-height:56px;letter-spacing:-1px}
.hero-sub{left:249px;top:254px;color:var(--white);font-size:28px;line-height:34px}
.btn-outline{display:block;border:1px solid var(--white);color:var(--white);font-size:11px;font-weight:700;text-align:center}
.hero-btn{left:249px;top:301px;width:120px;height:38px;line-height:36px}

/* decorative product areas */
.pendant{left:0;top:630px;width:122px;height:361px;background:linear-gradient(160deg,#f4e3a6 0%,#e0c062 50%,#c99f3a 100%)}
.rings{left:1000px;top:1522px;width:200px;height:200px;background:linear-gradient(135deg,#f1d27a 0%,#d4a83e 50%,#b7862a 100%)}

/* welcome */
.section-kicker{left:0;width:1200px;text-align:center}
.welcome-small{top:674px;font-size:17px;font-weight:800;color:var(--ink)}
.welcome-big{top:695px;font-size:27px;font-weight:800;color:var(--gold)}
.dots{left:586px;width:28px;height:12px}
.intro{left:320px;top:758px;width:560px;text-align:center;font-size:8.6px;line-height:18px;color:#666}

/* categories */
.cat{background:var(--soft)}
.shot{position:absolute}
.shot-gold{background:linear-gradient(180deg,#f1f1f1 0%,var(--gold-soft) 50%,#f1f1f1 100%)}
.shot-silver{background:linear-gradient(180deg,#f1f1f1 0%,var(--silver) 50%,#f1f1f1 100%)}
.shot-ruby{background:linear-gradient(180deg,#f1f1f1 0%,#d9b8a8 45%,#b5575f 60%,#f1f1f1 100%)}
.cat-label{position:absolute;width:96px;height:30px;background:var(--white);font-size:10px;font-weight:600;color:var(--ink);line-height:30px;padding-left:20px;overflow:hidden}
.cat-label::after{content:"";position:absolute;right:0;top:0;border-left:20px solid transparent;border-top:30px solid var(--gold)}

/* featured */
.featured-title{top:1210px;font-size:28px;font-weight:800;color:var(--gold)}
.featured-sub{top:1249px;font-size:11.5px;color:#555}
.tab{top:1313px;height:23px;background:var(--soft);font-size:9.5px;color:#555;text-align:center;line-height:23px}
.tab.is-active{background:var(--gold);color:var(--white);font-weight:700}
.product-img{top:1365px;width:163px;height:216px;background:var(--soft)}
.badge{width:30px;height:30px;border-radius:50%;background:var(--gold);color:var(--white);font-size:10px;font-weight:700;text-align:center;line-height:30px;z-index:1}
.product-name{top:1590px;font-size:11px;font-weight:700;color:var(--ink)}
.stars{top:1590px;font-size:9px;color:var(--gold);letter-spacing:-1px}
.product-desc{top:1611px;width:160px;font-size:8.5px;line-height:14px;color:#666}
.product-price{top:1643px;font-size:11px;font-weight:700;color:var(--ink)}
.arrow-btn{width:34px;height:34px;border-radius:50%;background:#2a2a2a}

/* banners */
.promo-left{left:0;top:1722px;width:579px;height:320px;background:linear-gradient(100deg,#7c3a4f 0%,#5c2d6d 45%,#4b2e8a 100%)}
.promo-right{left:621px;top:1722px;width:579px;height:320px;background:linear-gradient(90deg,#3a2a20 0%,#1f1612 55%,#4a3428 100%)}
.frame{left:313px;top:1776px;width:221px;height:210px;border:5px solid var(--white)}
.brush{left:276px;top:1800px;width:230px;height:180px;background:#2a4bb8;transform:skewX(-14deg);border-radius:6px;opacity:.95}
.promo-script{left:300px;top:1802px;width:250px;text-align:center;color:var(--white);font-size:24px;font-weight:700}
.promo-box{left:333px;top:1833px;width:184px;height:42px;background:var(--gold);color:var(--white);font-size:30px;font-weight:700;text-align:center;line-height:42px}
.promo-note{left:300px;top:1893px;width:250px;text-align:center;color:var(--white);font-size:10px}
.promo-btn{left:377px;top:1922px;width:96px;height:28px;line-height:26px;font-size:10px}
.crest{left:643px;top:1809px;width:240px;height:174px}
.crest-text{left:643px;width:240px;text-align:center;color:var(--gold);font-weight:800}
.crest-band{left:673px;top:1902px;width:180px;height:18px;background:var(--gold);color:var(--white);font-size:9px;text-align:center;line-height:18px}
.crest-link{left:643px;top:1936px;width:240px;text-align:center;font-size:10px;font-weight:700;color:var(--gold);text-decoration:underline}

/* services */
.services{left:0;top:2099px;width:1200px;height:162px;background:#f5f5f5}
.service-mid{left:397px;top:0;width:403px;height:162px;background:#f0f0f0;border:1px solid var(--line)}
.service{width:400px;text-align:center}
.service svg{display:block;margin:0 auto}
.service h3{font-size:14px;font-weight:700;color:var(--ink);margin-top:6px}
.service p{font-size:11px;color:#333}

/* footer */
.site-footer{left:0;top:2320px;width:1200px;height:254px;background:var(--footer);color:#aaa}
.foot-col h3{font-size:14px;font-weight:700;color:var(--white);margin-bottom:14px}
.foot-col p{font-size:9.5px;line-height:16px}
.foot-col ul{list-style:none;font-size:9.5px}
.foot-col li::before{content:"» ";color:#888}
.social{display:flex;gap:6px;margin-top:14px}
.social span{width:24px;height:24px;border-radius:50%;background:var(--gold)}
.news-input{left:784px;top:2443px;width:133px;height:30px;background:#333;font-size:9px;color:#777;line-height:30px;padding-left:10px}
.news-btn{left:917px;top:2443px;width:33px;height:30px;background:var(--gold)}
.bottom-bar{left:0;top:2574px;width:1200px;height:35px;background:var(--gold);color:var(--white);font-size:9.5px;line-height:35px;padding-left:249px}
</style>
</head>
<body>

<header class="site-header abs">
  <div class="brand abs"><span class="brand-dot"></span>VELISTO</div>
  <nav class="main-nav abs">
    <a style="left:0">Home</a>
    <a style="left:54px">Collections</a>
    <a style="left:134px">Product</a>
    <a style="left:197px">Blog</a>
    <a style="left:244px">Contact us</a>
  </nav>
  <div class="header-icons">
    <svg style="left:870px;top:52px" width="18" height="18" viewBox="0 0 18 18" fill="none" stroke="#999" stroke-width="1.5"><circle cx="7.5" cy="7.5" r="5.5"/><path d="M12 12l5 5"/></svg>
    <svg style="left:896px;top:50px" width="22" height="22" viewBox="0 0 22 22" fill="none" stroke="#999" stroke-width="1.5"><path d="M4 8h12l-1 10H5z"/><path d="M7 8a3 3 0 0 1 6 0"/><circle cx="17" cy="18" r="3.5" fill="var(--gold)" stroke="none"/></svg>
    <svg style="left:931px;top:52px" width="20" height="16" viewBox="0 0 20 16" fill="none" stroke="var(--gold)" stroke-width="1.3"><rect x="1" y="1" width="18" height="14"/><path d="M5 5h10M5 8h10M5 11h10"/></svg>
  </div>
</header>

<section class="hero abs">
  <div class="hero-photo abs" role="img" aria-label="Smiling woman with long flowing hair wearing a diamond necklace, drop earrings and a ring"></div>
  <div class="hero-tag abs">JEWELLERY</div>
  <h1 class="hero-title abs">YOU’LL FALL</h1>
  <p class="hero-sub abs">IN LOVE WITH</p>
  <a class="btn-outline hero-btn abs">Shop Now!</a>
</section>

<div class="account-menu abs">
  <h4>CURRENCY</h4>
  <ul><li>HKD</li><li>GBP</li><li>USD</li><li>EUR</li><li>RMB</li><li>JPY</li><li>AUD</li><li>CAD</li></ul>
  <h4 class="sec">MY ACCOUNT</h4>
  <hr>
  <ul style="margin-top:4px"><li>Log in</li><li>Register</li></ul>
</div>

<div class="pendant abs" role="img" aria-label="Gold heart pendant hanging on a chain"></div>

<h2 class="section-kicker welcome-small abs">WELCOME TO</h2>
<h2 class="section-kicker welcome-big abs">VELISTO JEWELLERY</h2>
<svg class="dots abs" style="top:737px" viewBox="0 0 28 12"><circle cx="10" cy="6" r="5" fill="var(--gold)"/><circle cx="19" cy="6" r="5" fill="none" stroke="#ddd"/></svg>
<p class="intro abs">Lorem Ipsum is simply dummy text of the printing and typesetting industry. Lorem Ipsum has been the industry's standard dummy text ever since the 1500s, when an unknown printer took a galley of type and scrambled it to make a type specimen book</p>

<div class="cat abs" style="left:249px;top:831px;width:165px;height:122px">
  <div class="shot shot-gold" style="left:10px;top:8px;width:145px;height:56px" role="img" aria-label="Gold pavé bangle bracelet"></div>
  <span class="cat-label" style="left:34px;top:72px">BRACELETS</span>
</div>
<div class="cat abs" style="left:249px;top:967px;width:165px;height:195px">
  <div class="shot shot-silver" style="left:10px;top:20px;width:145px;height:110px" role="img" aria-label="Pair of diamond stud earrings"></div>
  <span class="cat-label" style="left:34px;top:145px">EARRINGS</span>
</div>
<div class="abs" style="left:426px;top:831px;width:346px;height:331px;background:linear-gradient(135deg,#6d5a55 0%,#4a3a3a 55%,#2e2424 100%)" role="img" aria-label="Woman with dark hair wearing a gold necklace and rings">
  <span class="cat-label" style="left:14px;top:282px">RINGS</span>
</div>
<div class="cat abs" style="left:786px;top:831px;width:165px;height:195px">
  <div class="shot shot-ruby" style="left:10px;top:6px;width:145px;height:126px" role="img" aria-label="Ruby and diamond statement necklace"></div>
  <span class="cat-label" style="left:38px;top:145px">NECKLACES</span>
</div>
<div class="cat abs" style="left:786px;top:1040px;width:165px;height:122px">
  <div class="shot shot-silver" style="left:10px;top:10px;width:145px;height:54px" role="img" aria-label="Silver charm bracelet"></div>
  <span class="cat-label" style="left:38px;top:73px">CHARMS</span>
</div>

<h2 class="section-kicker featured-title abs">FEATURED PRODUCTS</h2>
<p class="section-kicker featured-sub abs">Lorem Ipsum is simply dummy text of the printing and typesetting industry</p>
<svg class="dots abs" style="top:1281px" viewBox="0 0 28 12"><circle cx="9" cy="6" r="5" fill="none" stroke="#ddd"/><circle cx="16" cy="6" r="5" fill="var(--gold)"/></svg>

<div class="tab is-active abs" style="left:417px;width:66px">Rings</div>
<div class="tab abs" style="left:492px;width:66px">Bracelets</div>
<div class="tab abs" style="left:567px;width:66px">Necklaces</div>
<div class="tab abs" style="left:642px;width:66px">Charms</div>
<div class="tab abs" style="left:716px;width:68px">Earrings</div>

<div class="product-img abs" style="left:249px">
  <div class="badge abs" style="left:8px;top:12px">-20</div>
  <div class="shot shot-silver" style="left:20px;top:40px;width:123px;height:140px" role="img" aria-label="Diamond solitaire ring"></div>
</div>
<div class="product-img abs" style="left:430px">
  <div class="shot shot-gold" style="left:12px;top:70px;width:139px;height:80px" role="img" aria-label="Gold pavé bangle"></div>
</div>
<div class="product-img abs" style="left:609px">
  <div class="badge abs" style="left:8px;top:12px">-45</div>
  <div class="shot shot-gold" style="left:30px;top:30px;width:103px;height:160px" role="img" aria-label="Gold fringe necklace"></div>
</div>
<div class="product-img abs" style="left:790px">
  <div class="shot shot-silver" style="left:12px;top:60px;width:139px;height:100px" role="img" aria-label="Diamond stud earrings"></div>
</div>

<svg class="arrow-btn abs" style="left:221px;top:1461px" viewBox="0 0 34 34"><path d="M19 11l-6 6 6 6" fill="none" stroke="#fff" stroke-width="2"/></svg>
<svg class="arrow-btn abs" style="left:945px;top:1461px" viewBox="0 0 34 34"><path d="M15 11l6 6-6 6" fill="none" stroke="#fff" stroke-width="2"/></svg>

<div class="product-name abs" style="left:249px">Rings</div><div class="stars abs" style="left:369px">★★★★★</div>
<div class="product-name abs" style="left:430px">Bracelets</div><div class="stars abs" style="left:550px">★★★★★</div>
<div class="product-name abs" style="left:609px">Necklaces</div><div class="stars abs" style="left:729px">★★★★★</div>
<div class="product-name abs" style="left:790px">Earrings</div><div class="stars abs" style="left:910px">★★★★★</div>
<p class="product-desc abs" style="left:249px">Lorem Ipsum is simply dummy text of the printing and typesetting industry</p>
<p class="product-desc abs" style="left:430px">Lorem Ipsum is simply dummy text of the printing and typesetting industry</p>
<p class="product-desc abs" style="left:609px">Lorem Ipsum is simply dummy text of the printing and typesetting industry</p>
<p class="product-desc abs" style="left:790px">Lorem Ipsum is simply dummy text of the printing and typesetting industry</p>
<div class="product-price abs" style="left:249px">$125.00</div>
<div class="product-price abs" style="left:430px">$231.00</div>
<div class="product-price abs" style="left:609px">$145.00</div>
<div class="product-price abs" style="left:790px">$251.00</div>

<div class="rings abs" role="img" aria-label="Pair of interlocked gold wedding bands"></div>

<section class="promo-left abs" role="img" aria-label="Woman with violet lipstick wearing a statement ring and earrings"></section>
<div class="brush abs"></div>
<div class="frame abs"></div>
<div class="promo-script abs">Velisto</div>
<div class="promo-box abs">Jewellery</div>
<p class="promo-note abs">50% off on Rings and Earrings Diamond</p>
<a class="btn-outline promo-btn abs">Shop Now!</a>

<section class="promo-right abs" role="img" aria-label="Woman with styled dark hair wearing long drop earrings"></section>
<svg class="crest abs" viewBox="0 0 240 174"><path d="M120 4 L200 34 L236 87 L200 140 L120 170 L40 140 L4 87 L40 34 Z" fill="#fff" stroke="var(--gold)" stroke-width="3"/><path d="M120 14 L193 41 L225 87 L193 133 L120 160 L47 133 L15 87 L47 41 Z" fill="none" stroke="var(--gold)" stroke-width="1"/></svg>
<div class="crest-text abs" style="top:1844px;font-size:14px">VELISTO</div>
<div class="crest-text abs" style="top:1862px;font-size:26px">JEWELLERY</div>
<div class="crest-band abs">25% off on Rings and Earrings Diamond</div>
<a class="crest-link abs">Shop Now!</a>

<section class="services abs">
  <div class="service-mid abs"></div>
  <div class="service abs" style="left:0;top:32px">
    <svg width="48" height="48" viewBox="0 0 48 48" fill="none" stroke="var(--gold)" stroke-width="1.6"><path d="M34 8c-8 2-14 8-18 16l8 8c8-4 14-10 16-18z"/><circle cx="29" cy="19" r="3"/><path d="M16 24l-6 2-2 6 8-2M24 32l-2 6 6-2 2-8M14 34l-6 6"/></svg>
    <h3>FREE SHIPPING &amp; RETURN</h3><p>Free shipping on orders over $49</p>
  </div>
  <div class="service abs" style="left:398px;top:32px">
    <svg width="48" height="48" viewBox="0 0 48 48" fill="none" stroke="var(--gold)" stroke-width="1.6"><path d="M18 8h12l-4 8h-4z"/><path d="M22 16c-10 4-14 12-14 18 0 6 6 8 16 8s16-2 16-8c0-6-4-14-14-18"/><path d="M27 25c-1-2-6-2-6 1s6 2 6 5-5 3-6 1M24 22v2M24 33v2"/></svg>
    <h3>MONEY GUARANTEE</h3><p>30 days money back guarantee</p>
  </div>
  <div class="service abs" style="left:800px;top:32px">
    <svg width="48" height="48" viewBox="0 0 48 48" fill="none" stroke="var(--gold)" stroke-width="1.6"><path d="M10 30v-6a14 14 0 0 1 28 0v6"/><rect x="8" y="26" width="7" height="12" rx="2"/><rect x="33" y="26" width="7" height="12" rx="2"/></svg>
    <h3>ONLINE SUPPORT</h3><p>We support online 24 hours a day</p>
  </div>
</section>

<footer class="site-footer abs">
  <div class="foot-col abs" style="left:249px;top:42px;width:200px">
    <h3>About us</h3>
    <p>Lorem Ipsum is simply dummy text of the printing and typesetting industry. Lorem Ipsum has been the industry's standard dummy text ever since the 1500s, when an unknown printer took a galley of type and scrambled it to make a type specimen book</p>
    <div class="social"><span></span><span></span><span></span><span></span></div>
  </div>
  <div class="foot-col abs" style="left:490px;top:42px">
    <h3>Shopping</h3>
    <ul style="line-height:24px"><li>My Wishlist</li><li>My Orders</li><li>Size Guide</li></ul>
  </div>
  <div class="foot-col abs" style="left:628px;top:42px">
    <h3>Customer Care</h3>
    <ul style="line-height:24px"><li>Delivery</li><li>Faqs</li><li>Returns</li><li>Care And Warranty</li><li>Contact us</li></ul>
  </div>
  <div class="foot-col abs" style="left:784px;top:42px;width:180px">
    <h3>Newsletters</h3>
    <p>Lorem Ipsum is simply dummy text of the printing and typesetting industry.</p>
  </div>
</footer>
<div class="news-input abs">Your Email Address</div>
<svg class="news-btn abs" viewBox="0 0 33 30"><path d="M10 15l14-6-4 14-3-5z" fill="#fff"/></svg>

<div class="bottom-bar abs">Copyright © 2017 <b>Velisto Jewellery</b> All Rights</div>

</body>
</html>
```